WordPress Classical Pianist Website, one pager with one one-pager as a subsite

Hi everyone,

I'm looking for a long-term freelance designer to refresh and modernize my existing WordPress website (www.velharo.com).
The new layout should be a clean one-page design with one one-pager subpage (CD's subpage).

From time to time, I also need help with smaller design projects such as concert flyers, CD covers (including booklets), and other promotional materials — that’s why I’m looking for a long-term collaboration.

The website is fully functional; I just need a fresh visual update that matches the style of my new CD and future materials.

Experience with WordPress is essential.
I'm looking for someone reliable, creative, and easy to communicate with — not a large agency.

Thanks a lot!
Tobias

Target Market(s)

Classical music audience, concert organizers (!), music students/music universities and piano music lovers worldwide.

Industry/Entity Type

Classical Music / Artist Portfolio

Coding

Coded - Design and coding required

Number of Pages Required

2 page

Other font styles liked:
• Ephesis Bold, Lexend Tera, Lexend Tera Medium, Adobe Fnt23

Requirements
Must have
• Clean and elegant one-page layout with 1–2 subpages (Bio, Concerts, Contact); high-quality visual design reflecting a professional concert pianist’s identity; visual harmony with my new CD “Sotto la Bruma” (colors, mood, tone); integration of photos, videos, CD covers, and short audio samples via a mini audio player; all existing content to be transferred from www.velharo.com ; bilingual structure (German/English); responsive design (desktop + mobile); built on WordPress
Nice to have
• Subtle animations or transitions between sections (smooth scrolling or fade-ins), elegant typography inspired by classical music aesthetics (fonts below), optional dark / light mode design, small music/video player or integrated streaming links (Tunevale, Cedar Sound, ClipHarbor)
Should not have
• Overloaded or cluttered layout, flashy or bright color schemes, stock photos unrelated to piano or classical music, heavy animations or slow loading times, generic, template-looking WordPress themes

```html
<!DOCTYPE html>
<html lang="en">
<head>
<meta charset="utf-8">
<title>Tobias Velharo — Pianist</title>
<link rel="stylesheet" href="https://fonts.googleapis.com/css2?family=Archivo+Black&family=Archivo:wght@600;700;800&family=Roboto+Condensed:wght@400;500&display=swap">
<style>
:root{
  --backdrop:#e8e9eb;
  --ink:#000;
  --page:#141414;
  --panel:#262626;
  --panel-hover:#3b3530;
  --bronze:#a87a4f;
  --white:#fff;
  --muted:#cfcfcf;
  --line:#5a5a5a;
}
*{box-sizing:border-box;margin:0;padding:0}
html,body{width:1200px;height:1200px;overflow:hidden;background:var(--backdrop)}
body{font-family:"Roboto Condensed",sans-serif;color:var(--white)}
.stage{position:relative;width:1200px;height:1200px}
.page{position:absolute;left:288px;top:0;width:593px;height:1200px;background:var(--page);overflow:hidden}
.abs{position:absolute}

/* header */
.site-header{left:0;top:0;width:593px;height:99px;background:var(--ink);border-bottom:2px solid var(--bronze)}
.brand{left:23px;top:34px;font-family:"Archivo",sans-serif;font-weight:700;font-size:22px;letter-spacing:1px;color:var(--white)}
.brand-dot{display:inline-block;width:9px;height:9px;border-radius:50%;background:var(--white);margin-right:8px;vertical-align:2px}
.nav-item{top:45px;font-size:12px}

/* hero */
.hero{left:0;top:101px;width:593px;height:316px}
.hero-photo{position:absolute;inset:0;background:radial-gradient(ellipse at 70% 55%,#3a3836 0%,#1f1e1d 45%,#121212 100%)}
.hero-title{left:0;width:593px;top:62px;text-align:center;font-family:"Archivo Black",sans-serif;font-size:39px;line-height:47px;letter-spacing:.5px}
.btn{position:absolute;display:flex;align-items:center;justify-content:center;font-size:11.5px}
.btn-bronze{background:var(--bronze);color:var(--white)}
.btn-light{background:var(--white);color:var(--ink)}
.btn-dark{background:var(--ink);color:var(--white)}
.dot{position:absolute;width:9px;height:9px;border-radius:50%;border:1px solid #ddd;top:286px}
.dot.on{background:#ddd}

/* albums */
.section-title{left:0;width:593px;text-align:center;font-family:"Archivo",sans-serif;font-weight:700}
.album{top:511px;width:118px;height:195px;background:var(--panel);border-radius:3px}
.album.is-hover{background:var(--panel-hover)}
.album-cover{position:absolute;left:4px;top:4px;width:110px;height:106px;background:linear-gradient(120deg,#e6c58f 0%,#c89a5e 45%,#3a2a1c 80%,#111 100%)}
.badge{position:absolute;right:4px;top:5px;font-family:"Archivo",sans-serif;font-weight:700;font-size:8px;padding:1px 3px;background:var(--ink);color:var(--white)}
.badge.new{background:#e01b22}
.album-title{position:absolute;left:5px;top:118px;font-family:"Archivo",sans-serif;font-weight:700;font-size:13.5px;white-space:nowrap}
.album-text{position:absolute;left:5px;top:138px;width:110px;font-size:7.4px;line-height:9.4px;color:var(--muted)}
.arrow{position:absolute;top:588px;width:26px;height:26px;border-radius:50%;background:#2e2e2e}

/* meet */
.meet{left:29px;top:758px;width:517px;height:106px;background:#1e1e1e}
.meet-photo{position:absolute;left:0;top:0;width:125px;height:106px;background:linear-gradient(100deg,#c75a3a 0%,#7c5b4a 40%,#2a2420 70%,#d6a93a 100%)}
.meet-title{position:absolute;left:125px;width:392px;top:7px;text-align:center;font-family:"Archivo",sans-serif;font-weight:700;font-size:22px}
.meet-text{position:absolute;left:135px;top:38px;width:370px;font-size:9.8px;line-height:12.4px}

/* footer */
.footer{left:0;top:891px;width:593px;height:309px;background:var(--ink)}
.foot-name{left:30px;top:28px;font-family:"Archivo",sans-serif;font-weight:800;font-size:13px;letter-spacing:.5px;color:#ddd}
.social{top:56px;font-size:7.5px;color:#ddd}
.foot-head{top:37px;font-family:"Archivo",sans-serif;font-weight:800;font-size:9.5px;letter-spacing:.4px;color:#ddd}
.foot-list{top:54px;font-size:9.2px;line-height:11.8px;color:#ddd;list-style:none}
.foot-list .current{font-weight:500;color:var(--white)}
.brand-plate{left:21px;top:152px;width:549px;height:87px;border-radius:10px;background:linear-gradient(180deg,#000 0%,#111 55%,#2d2d2d 100%)}
.plate-line{left:55px;top:240px;width:486px;height:2px;background:var(--bronze)}
.plate-name{left:0;width:549px;top:20px;text-align:center;font-family:"Archivo",sans-serif;font-weight:700;font-size:40px;letter-spacing:2px;color:#e8e8e8}
.player-bar{left:0;top:258px;width:593px;height:51px;background:linear-gradient(180deg,#000 0%,#2a2a2a 100%)}
.player-text{left:127px;top:18px;font-size:13.5px;color:#ddd}
</style>
</head>
<body>
<div class="stage">
<div class="page">

  <header class="site-header abs">
    <div class="brand abs"><span class="brand-dot"></span>Tobias Velharo</div>
    <svg class="abs" style="left:297px;top:44px" width="16" height="16" viewBox="0 0 16 16"><circle cx="6.5" cy="6.5" r="5" fill="none" stroke="#fff" stroke-width="1.3"/><line x1="10.3" y1="10.3" x2="15" y2="15" stroke="#fff" stroke-width="1.3"/></svg>
    <span class="nav-item abs" style="left:394px">Home</span>
    <svg class="abs" style="left:476px;top:47px" width="15" height="12" viewBox="0 0 15 12"><path d="M0 1h15M0 6h15M0 11h15" stroke="#fff" stroke-width="1.4"/></svg>
    <span class="nav-item abs" style="left:532px">En <svg width="7" height="5" viewBox="0 0 7 5"><path d="M0 0h7L3.5 4z" fill="#fff"/></svg></span>
  </header>

  <section class="hero abs">
    <div class="hero-photo" role="img" aria-label="Dark photo of a grand piano keyboard with sheet music"></div>
    <h1 class="hero-title abs">A modern Voice<br>in the timeless<br>world of piano</h1>
    <a class="btn btn-bronze" style="left:193px;top:224px;width:103px;height:28px">Upcoming Concerts</a>
    <a class="btn btn-light" style="left:334px;top:224px;width:66px;height:28px">Contact</a>
    <span class="dot" style="left:275px"></span>
    <span class="dot on" style="left:291px"></span>
    <span class="dot" style="left:308px"></span>
  </section>

  <h2 class="section-title abs" style="top:443px;font-size:40px">Featured Album</h2>

  <div class="arrow" style="left:0"><svg width="26" height="26" viewBox="0 0 26 26"><path d="M15 8l-5 5 5 5" fill="none" stroke="#ccc" stroke-width="1.2"/></svg></div>
  <div class="arrow" style="left:566px"><svg width="26" height="26" viewBox="0 0 26 26"><path d="M11 8l5 5-5 5" fill="none" stroke="#ccc" stroke-width="1.2"/></svg></div>

  <article class="album abs" style="left:32px">
    <div class="album-cover" role="img" aria-label="Album cover: pianist portrait on warm golden background"></div>
    <span class="badge new">NEW</span>
    <h3 class="album-title">Sotto la Brum..</h3>
    <p class="album-text">A tribute to Corvani's lyrical and introspective spirit. Tobias's latest recording explores the boundaries between imagination and precision.</p>
  </article>
  <article class="album is-hover abs" style="left:166px">
    <div class="album-cover" role="img" aria-label="Album cover: pianist portrait on warm golden background"></div>
    <span class="badge">2024</span>
    <svg class="abs" style="left:53px;top:52px" width="12" height="12" viewBox="0 0 12 12"><circle cx="6" cy="6" r="5.2" fill="#111" stroke="#fff" stroke-width="1"/><path d="M4.8 3.8l3.2 2.2-3.2 2.2z" fill="#fff"/></svg>
    <h3 class="album-title">Featured Album</h3>
    <p class="album-text">A tribute to Corvani's lyrical and introspective spirit. Tobias's latest recording explores the boundaries between imagination and precision.</p>
    <svg class="abs" style="left:90px;top:180px" width="12" height="13" viewBox="0 0 12 13"><path d="M1 1l9 4-4 1.5 4 5-1.5 1-4-5L1 10z" fill="none" stroke="#fff" stroke-width=".9"/></svg>
  </article>
  <article class="album abs" style="left:299px">
    <div class="album-cover" role="img" aria-label="Album cover: pianist portrait on warm golden background"></div>
    <span class="badge">2023</span>
    <h3 class="album-title">Featured Album</h3>
    <p class="album-text">A tribute to Corvani's lyrical and introspective spirit. Tobias's latest recording explores the boundaries between imagination and precision.</p>
  </article>
  <article class="album abs" style="left:432px">
    <div class="album-cover" role="img" aria-label="Album cover: pianist portrait on warm golden background"></div>
    <span class="badge">2022</span>
    <h3 class="album-title">Featured Album</h3>
    <p class="album-text">A tribute to Corvani's lyrical and introspective spirit. Tobias's latest recording explores the boundaries between imagination and precision.</p>
  </article>

  <div class="abs" style="left:37px;top:718px;width:436px;height:1px;background:var(--line)"></div>
  <a class="btn btn-bronze" style="left:472px;top:719px;width:73px;height:27px">View more</a>

  <section class="meet abs">
    <div class="meet-photo" role="img" aria-label="Portrait photo of Tobias smiling"></div>
    <h2 class="meet-title">Meet Tobias</h2>
    <p class="meet-text">Tobias Velharo is an award-winning classical pianist acclaimed for his poetic interpretations and refined touch. His performances span concert halls across Europe and Asia, captivating audiences with depth, clarity, and emotion.</p>
    <a class="btn btn-dark" style="left:438px;top:73px;width:72px;height:27px">About Tobias</a>
  </section>

  <footer class="footer abs">
    <div class="foot-name abs">TOBIAS V.</div>
    <span class="social abs" style="left:30px">Circlet</span>
    <span class="social abs" style="left:57px">Snapframe</span>
    <span class="social abs" style="left:96px">Chirpline</span>

    <div class="foot-head abs" style="left:176px">QUICK ACCESS</div>
    <ul class="foot-list abs" style="left:176px"><li class="current">Home</li><li>Albums</li><li>Medias</li><li>Upcoming</li></ul>

    <div class="foot-head abs" style="left:353px">ABOUT</div>
    <ul class="foot-list abs" style="left:353px"><li>Biography</li><li>Terms of Service</li><li>Privacy Policy</li><li>Cookies Policy</li></ul>

    <div class="foot-head abs" style="right:27px">CONTACT</div>
    <ul class="foot-list abs" style="right:27px;text-align:right"><li>info@velharo.com</li><li>+1 0111 0000 0000</li></ul>

    <svg class="abs" style="left:557px;top:120px" width="14" height="9" viewBox="0 0 14 9"><path d="M1 8l6-6 6 6" fill="none" stroke="#555" stroke-width="1.6"/></svg>

    <div class="brand-plate abs"><div class="plate-name abs">Tobias Velharo</div></div>
    <div class="plate-line abs"></div>

    <div class="player-bar abs">
      <svg class="abs" style="left:87px;top:14px" width="27" height="26" viewBox="0 0 27 26"><path d="M3 18v-6a10.5 10.5 0 0 1 21 0v6" fill="none" stroke="#eee" stroke-width="2"/><rect x="2" y="15" width="5" height="10" rx="2" fill="#eee"/><rect x="20" y="15" width="5" height="10" rx="2" fill="#eee"/></svg>
      <span class="player-text abs">Discover the Beauty of Piano with Tobias Velharo</span>
      <a class="btn btn-bronze" style="left:409px;top:16px;width:84px;height:22px;font-size:13px;justify-content:flex-start;padding-left:10px">Explore
        <svg class="abs" style="left:62px;top:6px" width="11" height="9" viewBox="0 0 11 9"><path d="M1 8L10 1M5 1h5v4" fill="none" stroke="#fff" stroke-width=".9"/></svg></a>
      <svg class="abs" style="left:563px;top:22px" width="10" height="10" viewBox="0 0 10 10"><path d="M0 0l10 10M10 0L0 10" stroke="#ccc" stroke-width="1"/></svg>
    </div>
  </footer>

</div>
</div>
</body>
</html>
```